Client Meeting and installation Email Follow up

I would like a follow-up email template created.
Currently, we do a lot of new construction builds and meet with clients about 6-3 months before they take possession of their new house. I want a follow-up email template to be sent after the homeowner takes possession of their house that enquires if the clients are happy about their new lighting, the service they received, and their customer service representative with Meridale Glow and Breeze. I have attached a few files of what our current marketing looks like.
Target Market(s)
Home Owners We have already met with
Industry/Entity Type
Residential lighting
Font styles to use
Other font styles liked:
- Alta Light, Playfair Display, Montserrat
Colors
Designer to choose colors to be used in the design.
Look and feel
Each slider illustrates characteristics of the customer's brand and the style your logo design should communicate.

```html
<!DOCTYPE html>
<html lang="en">
<head>
<meta charset="utf-8">
<title>Meridale Glow and Breeze – Lighting Follow-up Email</title>
<link rel="stylesheet" href="https://fonts.googleapis.com/css2?family=Jost:wght@300;400&family=Montserrat:wght@400;600&family=Playfair+Display:wght@400&display=swap">
<style>
  :root {
    --backdrop: #dfc9ca;
    --paper: #ffffff;
    --ink: #1d1d1d;
    --mocha: #a08270;
    --blush: #ead9d2;
    --mist: #f0f0f0;
    --charcoal: #2c2b2b;
    --cream-text: #f5e6de;
    --rule: #a8876f;
    --soft-text: #d8d3d0;
    --placeholder: #f3f2ef;
  }
  * { margin: 0; padding: 0; box-sizing: border-box; }
  html, body { width: 1200px; height: 4286px; overflow: hidden; }
  body { background: var(--backdrop); position: relative; font-family: "Montserrat", sans-serif; color: var(--ink); }
  .email { position: absolute; left: 191px; top: 161px; width: 816px; height: 3963px; background: var(--paper); overflow: hidden; }
  .abs { position: absolute; }
  .photo { position: absolute; border-radius: 6px; }

  .hero-photo { left: 34px; top: 0; width: 747px; height: 748px; border-radius: 0 0 8px 8px;
    background: linear-gradient(180deg, #e9d6d3 0%, #d8c4be 45%, #cdbfb5 70%, #c8c4c6 100%); }
  .brand-plate { left: 222px; top: 67px; width: 374px; height: 108px; background: var(--paper);
    display: flex; flex-direction: column; align-items: center; justify-content: center;
    font-family: "Jost", sans-serif; font-weight: 400; color: var(--ink); text-transform: uppercase; line-height: 1.05; }
  .brand-plate .line-one { font-size: 46px; letter-spacing: 1px; }
  .brand-plate .line-two { font-size: 26px; letter-spacing: 2px; }

  .intro { left: 0; top: 748px; width: 816px; height: 580px; text-align: center; }
  .intro .kicker { position: absolute; left: 0; width: 100%; top: 96px; font-family: "Jost", sans-serif; font-weight: 300; font-size: 52px; letter-spacing: 1px; }
  .intro .headline { position: absolute; left: 0; width: 100%; top: 170px; font-family: "Jost", sans-serif; font-weight: 300; font-size: 104px; line-height: 1; letter-spacing: 1px; }
  .intro .tag { position: absolute; left: 195px; top: 292px; width: 441px; height: 64px; border: 2px solid var(--rule);
    display: flex; align-items: center; justify-content: center; font-family: "Jost", sans-serif; font-size: 29px; letter-spacing: 6px; padding-left: 6px; }
  .rule { position: absolute; height: 2px; background: var(--rule); }
  .intro .rule { left: 238px; top: 397px; width: 340px; }
  .intro .lede { position: absolute; left: 140px; width: 536px; top: 432px; font-size: 25px; line-height: 34px; }

  .band { position: absolute; left: 0; width: 816px; }
  .band-feedback { top: 1328px; height: 513px; background: var(--mocha); }
  .band-feedback .note { position: absolute; left: 96px; width: 624px; top: 80px; text-align: center; color: var(--paper); font-size: 20.5px; line-height: 27px; }
  .band-service { top: 1841px; height: 562px; background: var(--blush); }
  .band-rep { top: 2403px; height: 531px; background: var(--mist); }
  .question { position: absolute; font-family: "Playfair Display", serif; font-size: 37px; line-height: 45px; }
  .q-lighting { left: 438px; top: 308px; width: 340px; color: var(--cream-text); }
  .q-service { left: 75px; top: 211px; width: 320px; color: var(--ink); }
  .q-rep { left: 438px; top: 152px; width: 340px; color: var(--ink); }

  .closing { position: absolute; left: 0; top: 2934px; width: 816px; height: 562px; text-align: center; }
  .closing .pledge { position: absolute; left: 60px; width: 696px; top: 158px; font-weight: 600; font-size: 29px; line-height: 41px; }
  .closing .rule { left: 238px; top: 294px; width: 340px; }
  .closing .offer { position: absolute; left: 125px; width: 566px; top: 337px; font-size: 25px; line-height: 35px; }
  .foliage { position: absolute; background: var(--placeholder); }

  .signoff { position: absolute; left: 0; top: 3496px; width: 816px; height: 467px; background: var(--charcoal); text-align: center; color: var(--soft-text); }
  .signoff .thanks { position: absolute; left: 110px; width: 596px; top: 85px; font-size: 18.5px; line-height: 27px; }
  .signoff .regards { position: absolute; left: 0; width: 100%; top: 187px; font-family: "Jost", sans-serif; font-weight: 300; font-size: 50px; color: var(--paper); letter-spacing: 1px; }
  .signoff .team { position: absolute; left: 0; width: 100%; top: 262px; font-size: 18.5px; }
  .signoff .social { position: absolute; left: 373px; top: 324px; width: 70px; height: 30px; }
  .signoff .divider { position: absolute; left: 34px; top: 392px; width: 748px; height: 1px; background: #55514f; }
  .signoff .site { position: absolute; left: 0; width: 100%; top: 416px; font-size: 18.5px; }
</style>
</head>
<body>
  <main class="email">
    <div class="photo hero-photo" role="img" aria-label="Bright blush-pink attic home office with a crystal chandelier, twin desks and a wooden table"></div>
    <div class="abs brand-plate">
      <span class="line-one">Meridale</span>
      <span class="line-two">Glow and Breeze</span>
    </div>

    <section class="abs intro">
      <p class="kicker">HOW ARE YOU</p>
      <h1 class="headline">ENJOYING</h1>
      <p class="tag">YOUR NEW LIGHTING?</p>
      <div class="rule"></div>
      <p class="lede">We hope you’re enjoying your recently installed lighting!</p>
    </section>

    <section class="band band-feedback">
      <p class="note">Now that some time has passed, we wanted to check in and see how the lighting is working out for you. Your satisfaction is very important to us, and we’d love to hear your feedback on the following:</p>
      <p class="question q-lighting">Are you happy with the lighting in your space?</p>
    </section>
    <div class="photo" style="left:75px; top:1575px; width:325px; height:357px; background:linear-gradient(160deg,#e8e2da 0%,#cdbba6 40%,#4a3f38 80%,#2e2a28 100%);" role="img" aria-label="Kitchen corner with white subway tile, wooden open shelves and a table lamp"></div>

    <section class="band band-service">
      <p class="question q-service">Was our<br>service during the<br>installation<br>process<br>satisfactory?</p>
    </section>
    <div class="photo" style="left:435px; top:1971px; width:324px; height:356px; background:linear-gradient(170deg,#f3f1ec 0%,#e2d6c4 45%,#9a7b52 70%,#2f4f4a 100%);" role="img" aria-label="Breakfast nook with a globe pendant, framed art and a teal banquette"></div>

    <section class="band band-rep">
      <p class="question q-rep">How was your experience with your Meridale Glow and Breeze representative?</p>
    </section>
    <div class="photo" style="left:75px; top:2485px; width:325px; height:357px; background:linear-gradient(150deg,#ebe7e1 0%,#d9d4cc 45%,#c99a55 70%,#6f6a5f 100%);" role="img" aria-label="Cluster of white dome pendant lights with warm gold interiors"></div>

    <section class="closing">
      <div class="foliage" style="left:0; top:0; width:150px; height:230px;" role="img" aria-label="Corner foliage decoration"></div>
      <div class="foliage" style="left:690px; top:370px; width:126px; height:192px;" role="img" aria-label="Corner foliage decoration"></div>
      <p class="pledge">We’re committed to providing the best<br>possible service and are always looking<br>for ways to improve.</p>
      <div class="rule"></div>
      <p class="offer">If there’s anything we can do to assist further or if you have any concerns, please don’t hesitate to reach out.</p>
    </section>

    <footer class="signoff">
      <p class="thanks">Thank you once again for choosing Meridale Glow and Breeze. We look forward to hearing from you and hope to work with you again in the future!</p>
      <p class="regards">WARM REGARDS,</p>
      <p class="team">“Meridale Glow and Breeze Team”</p>
      <svg class="social" viewBox="0 0 70 30" aria-label="Social links">
        <circle cx="15" cy="15" r="14" fill="#eeeeee"/>
        <circle cx="55" cy="15" r="14" fill="#eeeeee"/>
      </svg>
      <div class="divider"></div>
      <p class="site">www.meridaleglow.com</p>
    </footer>
  </main>
</body>
</html>
```